Business Card Design Project

We need a business card design for a new construction company called 'KORVA HOLDINGS PTY.LTD' We run a construction based company for high end market homes in melbourne, we want something that looks professional and eye catching.The card needs to have a strong design to it something modern as the company name explains "korva." The final design should communicate professionalism and a strong image to our customers on the quality of our work.
On the business card i need
Name: Marek Holtvay
Mob:0417295031
Email:korva.holdings@mailbrook.example
Domestic/Residential/Commercial

```html
<!DOCTYPE html>
<html lang="en">
<head>
<meta charset="utf-8">
<title>Korva Holdings – Business Card</title>
<link rel="stylesheet" href="https://fonts.googleapis.com/css2?family=Fjalla+One&family=Source+Sans+3:wght@400&display=swap">
<style>
  :root {
    --sheet: #ffffff;
    --gold-light: #d6bc2a;
    --gold-mid: #c0912a;
    --gold-deep: #a8681f;
    --ink: #1d1d1b;
    --brand-red: #e3262a;
    --cream: #efd9b4;
    --label: #111111;
  }
  * { margin: 0; padding: 0; box-sizing: border-box; }
  html, body {
    width: 1200px; height: 982px; overflow: hidden;
    background: var(--sheet);
  }
  .sheet { position: relative; width: 1200px; height: 982px; }

  .card {
    position: absolute; width: 826px; height: 471px; overflow: hidden;
    font-family: "Fjalla One", "Arial Narrow", sans-serif;
  }
  .card--front { left: 11px; top: 14px; }
  .card--back { left: 370px; top: 501px; }

  .card__background {
    position: absolute; inset: 0;
    background: radial-gradient(ellipse 70% 75% at 50% 50%, var(--gold-light) 0%, var(--gold-mid) 55%, var(--gold-deep) 100%);
  }
  .card--back .card__background {
    background: radial-gradient(ellipse 65% 70% at 50% 52%, var(--gold-light) 0%, var(--gold-mid) 55%, var(--gold-deep) 100%);
  }

  .brand { position: absolute; text-align: center; }
  .brand__name { display: block; line-height: 1; text-transform: lowercase; }
  .brand__tagline { display: block; letter-spacing: 0.32em; white-space: nowrap; }

  .card--front .brand { left: 240px; top: 112px; width: 370px; }
  .card--front .brand__name { font-size: 124px; color: var(--ink); }
  .card--front .brand__tagline { font-size: 15px; color: var(--brand-red); margin-top: 4px; }

  .card--back .brand { left: 16px; top: 16px; width: 280px; opacity: 0.75; }
  .card--back .brand__name { font-size: 88px; color: var(--cream); }
  .card--back .brand__tagline { font-size: 12px; color: var(--cream); margin-top: 2px; }

  .contact {
    position: absolute; right: 30px; top: 40px; width: 380px;
    text-align: center; color: var(--ink);
  }
  .contact__name { font-size: 56px; line-height: 1.05; }
  .contact__phone { font-size: 44px; line-height: 1.05; letter-spacing: 0.01em; }

  .services {
    position: absolute; left: 48px; top: 160px;
    list-style: none; color: #2a2620;
    font-size: 46px; line-height: 52px;
  }

  .email {
    position: absolute; left: 66px; bottom: 26px;
    display: flex; align-items: baseline; gap: 20px; white-space: nowrap;
  }
  .email__label { font-size: 50px; color: var(--cream); }
  .email__address { font-size: 37px; color: var(--ink); }

  .side-label {
    position: absolute; font-family: "Source Sans 3", "Myriad Pro", sans-serif;
    font-size: 70px; color: var(--label); line-height: 1;
  }
  .side-label--front { left: 890px; top: 176px; }
  .side-label--back { left: 60px; top: 692px; }
</style>
</head>
<body>
<main class="sheet">
  <section class="card card--front" aria-label="Card front">
    <div class="card__background" role="img" aria-label="Golden radial gradient background with soft circular cluster pattern"></div>
    <div class="brand">
      <span class="brand__name">korva</span>
      <span class="brand__tagline">KORVA HOLDINGS PTY.LTD</span>
    </div>
  </section>

  <p class="side-label side-label--front">&lt; front</p>
  <p class="side-label side-label--back">back &gt;</p>

  <section class="card card--back" aria-label="Card back">
    <div class="card__background" role="img" aria-label="Golden radial gradient background with faint circular cluster pattern"></div>
    <div class="brand">
      <span class="brand__name">korva</span>
      <span class="brand__tagline">KORVA HOLDINGS PTY.LTD</span>
    </div>
    <div class="contact">
      <p class="contact__name">Marek Holtvay</p>
      <p class="contact__phone">0417295031</p>
    </div>
    <ul class="services">
      <li>Domestic</li>
      <li>Residential</li>
      <li>Commercial</li>
    </ul>
    <p class="email">
      <span class="email__label">Email:</span>
      <span class="email__address">korva.holdings@mailbrook.example</span>
    </p>
  </section>
</main>
</body>
</html>
```